Travel Adventure Challenge Poster/Information Sheet

We have created a corporate incentive travel package we’ve called the “The Quest Horizon Link” This is an experiential travel adventure,….not a tour, an adventure designed to awaken the senses, tap into your realm of creativity and resourcefulness, and connect you with a new environment.
“X” for the mystery, as in, “the unknown”
“Challenge” for the competitive element: - each day offers a competitive challenge that calls forth creativity, resourcefulness and team interaction.
“Connection” for the experience of truly relating to the culture that the participant is emerged in.
We require a one-pager (A4) 8.5x11, one-sided informative ad that is directed toward corporate incentive travel clientele and adventure enthusiasts. I've attached 2 logo's One for the event itself and the other for the parent company. (The Quest Horizon Link and Bespoke Journey Services) This is a teaser. The goal is to have people contact us by phone, web, or email to find out more information. I've also attached several pages of content and images to choose from...The green, black/grey and white are the standard colors for the logo and we are open to incorporating vibrant complementary colors. Let your creativity flow! We look forward to seeing what you can create!

```html
<!DOCTYPE html>
<html lang="en">
<head>
<meta charset="utf-8">
<title>Quest Horizon Link – Compete. Create. Connect.</title>
<link rel="stylesheet" href="https://fonts.googleapis.com/css2?family=Montserrat:wght@600;700&family=Roboto+Condensed:wght@400;700&family=Open+Sans:wght@400;600&display=swap">
<style>
  :root {
    --stage: #7dff0a;
    --lime: #66f200;
    --lime-light: #a8ff2a;
    --lime-deep: #2f9a00;
    --forest: #124a10;
    --charcoal: #3b4242;
    --ink: #1f2a1f;
    --white: #ffffff;
    --slate: #56606a;
  }
  * { box-sizing: border-box; margin: 0; padding: 0; }
  html, body { width: 1200px; height: 1000px; overflow: hidden; }
  body { background: var(--stage); position: relative; font-family: "Open Sans", Arial, sans-serif; }

  .flyer {
    position: absolute; left: 264px; top: 65px;
    width: 672px; height: 870px;
    background: var(--lime); overflow: hidden;
  }
  .flyer-backdrop { position: absolute; inset: 0; width: 672px; height: 616px; }

  .hero-photo {
    position: absolute; left: 330px; top: 0; width: 342px; height: 200px;
    background: linear-gradient(160deg, rgba(60,120,40,.9), rgba(20,70,20,.6) 60%, rgba(20,70,20,0));
  }

  .event-name {
    position: absolute; left: 0; top: 20px; width: 277px; height: 60px;
    background: var(--white); display: flex; align-items: center; padding-left: 34px;
    font-family: "Roboto Condensed", sans-serif; font-weight: 700; font-size: 19px;
    color: var(--ink); letter-spacing: .5px; text-transform: uppercase;
  }

  .headline {
    position: absolute; left: 0; width: 672px; top: 112px; text-align: center;
    padding-left: 40px;
    font-family: "Montserrat", sans-serif; font-weight: 700; font-size: 33px;
    color: var(--white); letter-spacing: 1px;
  }
  .subhead {
    position: absolute; left: 105px; top: 156px;
    font-family: "Roboto Condensed", sans-serif; font-weight: 700; font-size: 15px;
    color: #e9ffd0; letter-spacing: .4px;
  }

  .intro {
    position: absolute; left: 22px; top: 205px; width: 170px;
    font-size: 12.5px; line-height: 19.5px; color: var(--ink);
  }
  .intro p + p { margin-top: 18px; }

  .gallery .shot {
    position: absolute; border: 3px solid var(--white);
    box-shadow: 3px 4px 8px rgba(0,0,0,.45);
  }
  .shot.rainforest { left: 207px; top: 197px; width: 102px; height: 66px; background: linear-gradient(135deg,#2e5d1f,#6a9b3a); }
  .shot.hillside   { left: 277px; top: 262px; width: 102px; height: 70px; background: linear-gradient(135deg,#5a8a2a,#9cc25a); }
  .shot.resort     { left: 210px; top: 344px; width: 102px; height: 80px; background: linear-gradient(135deg,#7a4a2a,#c9a06a 60%,#4aa0a8); }
  .shot.culture    { left: 277px; top: 427px; width: 102px; height: 78px; background: linear-gradient(135deg,#3a8a3a,#d84a3a 50%,#6ab0d8); }
  .shot.cooking    { left: 197px; top: 500px; width: 102px; height: 72px; background: linear-gradient(135deg,#d8c8b0,#8a5a3a); }

  .pillars {
    position: absolute; left: 417px; top: 208px; width: 250px;
    font-size: 12.5px; line-height: 19.5px; color: var(--white);
    text-shadow: 0 1px 2px rgba(0,0,0,.35);
  }
  .pillars p + p { margin-top: 16px; }
  .pillar-title {
    font-family: "Roboto Condensed", sans-serif; font-weight: 700; font-size: 18px;
    color: var(--lime-light); text-transform: uppercase;
  }

  .parent-brand {
    position: absolute; left: 370px; top: 557px; width: 302px; height: 59px;
  }
  .parent-brand svg { position: absolute; inset: 0; }
  .parent-brand span {
    position: absolute; left: 100px; top: 10px; width: 110px;
    font-family: "Roboto Condensed", sans-serif; font-weight: 700; font-size: 12px;
    line-height: 13px; color: var(--slate); text-transform: uppercase;
  }

  .promise {
    position: absolute; left: 0; top: 616px; width: 672px; height: 142px;
    background: var(--charcoal); text-align: center; color: var(--white);
    padding: 10px 40px 0;
  }
  .promise-text { font-size: 14.5px; line-height: 20px; }
  .promise-offer {
    margin-top: 12px; font-weight: 600; font-size: 20.5px; line-height: 30px;
    color: var(--lime-light);
  }

  .dates {
    position: absolute; left: 0; top: 758px; width: 672px; height: 48px;
    background: var(--lime-light); text-align: center;
    font-family: "Roboto Condensed", sans-serif; font-size: 27px; line-height: 48px;
    color: var(--white);
  }

  .contact {
    position: absolute; left: 0; top: 806px; width: 672px; height: 64px;
    background: var(--charcoal); text-align: center; color: var(--white);
    font-size: 14px; line-height: 20px; padding-top: 11px;
  }
</style>
</head>
<body>
  <article class="flyer">
    <svg class="flyer-backdrop" viewBox="0 0 672 616" aria-hidden="true">
      <polygon points="0,0 672,0 672,616 0,616" fill="#66f200"/>
      <polygon points="120,616 300,300 420,616" fill="#4fd800" opacity=".7"/>
      <polygon points="0,380 200,616 0,616" fill="#8aff2a" opacity=".6"/>
      <polygon points="400,0 672,0 672,616 400,616 390,300" fill="#1f5e16" opacity=".85"/>
      <polygon points="330,0 500,0 420,300 390,290" fill="#2f8a14" opacity=".6"/>
      <polygon points="390,300 300,616 420,616" fill="#9cff3b" opacity=".55"/>
    </svg>

    <div class="hero-photo" role="img" aria-label="Photo of a businessman crouched at a starting line, ready to race"></div>

    <div class="event-name">Quest Horizon Link</div>

    <h1 class="headline">COMPETE. CREATE. CONNECT.</h1>
    <p class="subhead">TRAVEL DESIGNED TO REVIVE AND EXPAND CREATIVE THINKING</p>

    <div class="intro">
      <p>When 1,500 of the top CEO’s from around the world were interviewed, they believed that more than rigor, management, discipline, integrity or even vision, creativity ranked number one.</p>
      <p>The Quest Horizon Link has designed a cultural playground for the mind to explore its creative pipeline, incorporating daily challenges that excite, engage, interact and educate.</p>
    </div>

    <div class="gallery">
      <div class="shot rainforest" role="img" aria-label="Photo of a traveller on a rainforest canopy bridge"></div>
      <div class="shot hillside" role="img" aria-label="Photo of a green tropical hillside"></div>
      <div class="shot resort" role="img" aria-label="Photo of a luxury resort pool and pavilion"></div>
      <div class="shot culture" role="img" aria-label="Photo of women in traditional dress beneath lanterns"></div>
      <div class="shot cooking" role="img" aria-label="Photo of a group at a cooking class"></div>
    </div>

    <div class="pillars">
      <p><span class="pillar-title">Compete.</span> Daily mystery challenges have each participant fully immersed and engaged in a stimulating and educational environment designed to build team skills, leadership and expand creativity while competing daily for prize rewards.</p>
      <p><span class="pillar-title">Create.</span> Explore cuisine, language, history and communities.</p>
      <p><span class="pillar-title">Connect.</span> Side by side, with your teammate and the Quest Horizon crew, you will intimately explore culture, address challenges and build strategies that you can apply to day-to-day living, while having the time of your life!</p>
    </div>

    <div class="parent-brand">
      <svg viewBox="0 0 302 59" aria-hidden="true"><polygon points="0,0 302,0 302,59 60,59" fill="#ffffff"/></svg>
      <span>Bespoke Journey Services</span>
    </div>

    <section class="promise">
      <p class="promise-text">Your Quest Horizon team is on the ground beside you ensuring that each element of the event is managed to perfection. We promise that when the daily challenge is complete, luxurious accommodation and relaxation are waiting!</p>
      <p class="promise-offer">Experience a 5* - 10 day mystery challenge immersed in the vibrancy of Vietnam or Costa Rica.</p>
    </section>

    <div class="dates">Vietnam October 2014 Costa Rica November 2014</div>

    <footer class="contact">
      <p>Contact us to learn more. hello@bespokejs.cc 1.800.555.0147 x 210</p>
      <p>www.questhorizonlink.com</p>
    </footer>
  </article>
</body>
</html>
```